Landingpage Design X-Mas Invitation

Every year we invite customers to a special X-Mas Apéro. Since we are an IT-Company we handle the registration process by a landingpage. For this we need a design for the event 2016. The content will be the same as 2015 (you will finde the design attached from last year. There will be an additional job for creating the E-Mail.

Target Market(s)

Customers of IT Company, medium Companys in Central Switzerland

Industry/Entity Type

It Company

Number of Pages Required

1 page

Requirements
Must have
• Christmas Style

```html
<!DOCTYPE html>
<html lang="de">
<head>
<meta charset="utf-8">
<title>Lindmark Weihnachtsapéro 2016</title>
<link href="https://fonts.googleapis.com/css2?family=Montserrat:wght@500&family=Roboto:wght@400;500;700&family=Lato:ital,wght@1,400&display=swap" rel="stylesheet">
<style>
:root{
  --brand-red:#c0302a;
  --deep-red:#a3191a;
  --form-red:#c43a30;
  --ink:#222;
  --footer:#232323;
  --footer-bottom:#1d1d1d;
  --white:#fff;
  --muted:#ddd;
  --partner:#c9ccd1;
}
*{margin:0;padding:0;box-sizing:border-box}
html,body{width:916px;height:1200px;overflow:hidden;background:var(--white)}
body{position:relative;font-family:'Roboto',Arial,sans-serif;color:var(--ink)}
.page{position:relative;width:916px;height:1200px}
.topline{position:absolute;top:0;left:0;width:916px;height:3px;background:var(--brand-red)}
.header{position:absolute;top:3px;left:0;width:916px;height:83px;background:var(--white)}
.brand{position:absolute;text-align:right;font-family:'Roboto',Arial,sans-serif;font-weight:700;line-height:1}
.brand-name{display:block;font-size:34px;letter-spacing:-.5px}
.brand-sub{display:block;font-size:9px;font-weight:400;letter-spacing:.8px;margin-top:2px}
.header .brand{left:386px;top:22px;color:var(--brand-red)}
.header .brand-sub{color:var(--ink)}
.hero{position:absolute;top:86px;left:0;width:916px;height:562px;background:#000}
.hero-photo{position:absolute;inset:0;background:
  radial-gradient(circle at 22% 35%,rgba(190,110,40,.75),transparent 45%),
  radial-gradient(circle at 10% 70%,rgba(120,40,20,.7),transparent 50%),
  radial-gradient(circle at 35% 15%,rgba(160,60,30,.6),transparent 40%),
  linear-gradient(90deg,#3a1a0e 0%,#2a0f08 40%,#0a0504 60%,#000 75%)}
.hero-text{position:absolute;left:470px;top:92px;width:400px;color:var(--white)}
.hero-title{font-family:'Montserrat',Arial,sans-serif;font-weight:500;font-size:21px;line-height:25.5px;margin-bottom:25px}
.hero-body{font-size:12.5px;line-height:17px;margin-top:36px}
.hero-body p{margin-bottom:16px}
.partners{position:absolute;top:648px;left:0;width:916px;height:108px;background:var(--white);display:flex;align-items:center;justify-content:space-between;padding:0 48px}
.partner{background:var(--partner);height:22px;border-radius:3px}
.partner.round{width:30px;height:30px;border-radius:50%}
.registration{position:absolute;top:756px;left:0;width:916px;height:269px;background:linear-gradient(135deg,#c84237 0%,#c13a2f 50%,#b23026 100%)}
.form-col{position:absolute;top:52px;width:378px}
.form-col.left{left:68px}
.form-col.right{left:473px}
.form-title{font-family:'Lato',Arial,sans-serif;font-style:italic;font-size:19px;color:var(--white);margin:0 0 18px 2px;height:22px}
.field{display:block;height:30px;border-radius:15px;background:var(--white);font-size:10px;color:#444;padding:0 20px;line-height:30px;margin-bottom:10px}
.row{display:flex;gap:13px}
.row .field{flex:1}
.submit{display:block;width:119px;height:32px;border:0;border-radius:16px;background:var(--deep-red);color:var(--white);font-family:'Roboto',Arial,sans-serif;font-weight:500;font-size:14px;margin-top:6px}
.footer{position:absolute;top:1025px;left:0;width:916px;height:108px;background:var(--footer);color:var(--white)}
.footer .brand{left:57px;top:35px;color:var(--white)}
.footer .brand-name{font-size:32px}
.contact{position:absolute;top:40px;display:flex;align-items:center;gap:10px;font-size:10.5px;line-height:17px}
.contact svg{flex:none}
.contact strong{font-size:13px;font-weight:700}
.legal{position:absolute;top:1133px;left:0;width:916px;height:67px;background:var(--footer-bottom);border-top:1px solid #333;color:var(--muted);font-size:10px;text-align:center;line-height:67px}
</style>
</head>
<body>
<div class="page">
  <div class="topline"></div>
  <header class="header">
    <div class="brand"><span class="brand-name">Lindmark</span><span class="brand-sub">IT SOLUTIONS</span></div>
  </header>

  <section class="hero">
    <div class="hero-photo" role="img" aria-label="Weihnachtskugel mit bunten Lichtern in warmem Bokeh"></div>
    <div class="hero-text">
      <h1 class="hero-title">Lindmark Weihnachtsapéro<br>and the Event Informations:</h1>
      <p class="hero-title">Donnerstag, 15.12.2016<br>ab 17.00 Uhr</p>
      <p class="hero-title">Lindmark Skylounge, Seeblick-<br>strasse 12, 6004 Luzern</p>
      <div class="hero-body">
        <p>Ob Sie den ganzen Abend bleiben oder nur kurz nach dem Weihnachts-Shopping vorbeischauen, ist ganzIhnen uberlassen.</p>
        <p>Wir freuen uns sehr, wenn Sie uns die Gelegenheit geben, Ihnen mit dieser Einladung for die</p>
        <p>erfolgreiche Zusammenarbeit herzlichst zu danken.</p>
      </div>
    </div>
  </section>

  <section class="partners" aria-label="Partner">
    <span class="partner round"></span>
    <span class="partner" style="width:98px"></span>
    <span class="partner" style="width:52px"></span>
    <span class="partner" style="width:36px"></span>
    <span class="partner" style="width:97px"></span>
    <span class="partner" style="width:64px"></span>
    <span class="partner" style="width:53px"></span>
    <span class="partner" style="width:72px"></span>
    <span class="partner" style="width:48px"></span>
    <span class="partner" style="width:63px"></span>
    <span class="partner" style="width:87px"></span>
  </section>

  <section class="registration" role="img" aria-label="Hände an einer Tastatur in Rot getönt">
    <form class="form-col left">
      <h2 class="form-title">Ihre Anmeldung</h2>
      <span class="field">Ihre E-mail-Adresse</span>
      <div class="row"><span class="field">Vorname</span><span class="field">Nachname</span></div>
      <button class="submit" type="button">Absenden</button>
    </form>
    <div class="form-col right">
      <h2 class="form-title">Ihre Begleitperson</h2>
      <span class="field">Firma (Optional)</span>
      <div class="row"><span class="field">Vorname</span><span class="field">Nachname</span></div>
    </div>
  </section>

  <footer class="footer">
    <div class="brand"><span class="brand-name">Lindmark</span><span class="brand-sub">IT SOLUTIONS</span></div>
    <div class="contact" style="left:256px;width:250px">
      <svg width="28" height="28" viewBox="0 0 28 28"><circle cx="14" cy="14" r="13" fill="none" stroke="#fff" stroke-width="1"/><path d="M14 8a4 4 0 0 0-4 4c0 3 4 8 4 8s4-5 4-8a4 4 0 0 0-4-4z" fill="none" stroke="#fff" stroke-width="1.4"/><circle cx="14" cy="12" r="1.3" fill="#fff"/></svg>
      <span>KONTAKT :&nbsp;&nbsp; Lindmark IT Solutions AG Seeblick-<br>strasse 12 6004 Luzern</span>
    </div>
    <div class="contact" style="left:552px">
      <svg width="28" height="28" viewBox="0 0 28 28"><circle cx="14" cy="14" r="13" fill="none" stroke="#fff" stroke-width="1"/><path d="M10 8.5l2.2-.5 1.3 3-1.4 1a7 7 0 0 0 3.4 3.4l1-1.4 3 1.3-.5 2.2c-5.5.3-9.3-3.5-9-9z" fill="#fff"/></svg>
      <span>Telefon:<br><strong>1800 300 5120</strong></span>
    </div>
    <div class="contact" style="left:731px">
      <svg width="28" height="28" viewBox="0 0 28 28"><circle cx="14" cy="14" r="13" fill="none" stroke="#fff" stroke-width="1"/><rect x="8.5" y="10" width="11" height="8" rx="1" fill="none" stroke="#fff" stroke-width="1.3"/><path d="M8.5 10.5l5.5 4 5.5-4" fill="none" stroke="#fff" stroke-width="1.3"/></svg>
      <span>Email:<br>info@lindmark-it.example</span>
    </div>
  </footer>
  <div class="legal">Copyright ©, Lindmark.&nbsp; All Rights Reserved.</div>
</div>
</body>
</html>
```